TriVex Business Card Design - double sided -plumbing local plumbing company

We have a Plumbing company where the design was create through Sketch Hive. We would now like a business card designed as well. We want it to be in the colour version of the logo.

Details below for the card.

Phone Number: 0438 615 247
Email: info@trivexplumbing.example.au
Website: https://trivexplumbing.example.au
We really want a sophisticated design that stand out from the other- informative and timeless.

Target Market(s)

local Canberra market

Industry/Entity Type

Plumbing, gas fitting, hot water

Contact Information for Business Card

Phone number, email, logo and "Supplying all your heating, cooling and hot water needs"

Requirements
Must have
• bust be colourful, must also be though about it being printed on a magnet. must Vex with the logo - I dont want the logo and information chucked onto a white canvas I would prefer it to be smooth and look purposeful

```html
<!DOCTYPE html>
<html lang="en">
<head>
<meta charset="utf-8">
<title>TriVex Business Card</title>
<link rel="stylesheet" href="https://fonts.googleapis.com/css2?family=Lato:wght@400;700;900&display=swap">
<style>
  :root {
    --page-bg: #1f2024;
    --navy: #041d3c;
    --sky: #05a8e6;
    --orange: #f7a83b;
    --white: #ffffff;
    --grey: #6b6b6b;
  }
  * { margin: 0; padding: 0; box-sizing: border-box; }
  html, body { width: 1200px; height: 952px; overflow: hidden; }
  body {
    background: var(--page-bg);
    font-family: "Lato", sans-serif;
    position: relative;
  }
  .card {
    position: absolute;
    top: 311px;
    width: 540px;
    height: 330px;
    overflow: hidden;
    box-shadow: 0 12px 30px rgba(0,0,0,0.45);
  }
  /* Back side */
  .card-back { left: 40px; background: var(--navy); }
  .card-back .corner { position: absolute; inset: 0; }
  .card-back .wordmark {
    position: absolute;
    left: 0; right: 0; top: 50%;
    transform: translateY(-50%);
    text-align: center;
    font-size: 72px;
    font-weight: 900;
    color: var(--sky);
    letter-spacing: 2px;
  }
  /* Front side */
  .card-front { left: 620px; background: var(--white); }
  .card-front .wordmark {
    position: absolute;
    left: 40px; top: 30px;
    font-size: 54px;
    font-weight: 900;
    color: var(--sky);
    letter-spacing: 1px;
  }
  .person { position: absolute; left: 42px; top: 112px; }
  .person-name {
    font-size: 19px;
    letter-spacing: 1px;
    color: var(--sky);
    font-weight: 400;
  }
  .person-name .surname { color: var(--orange); font-weight: 900; }
  .person-role { font-size: 14px; color: var(--grey); margin-top: 2px; }
  .contact-band {
    position: absolute;
    left: 28px; top: 172px;
    width: 390px; height: 88px;
    background: var(--sky);
    display: flex;
  }
  .icon-strip {
    width: 30px;
    background: var(--orange);
    display: flex;
    flex-direction: column;
    justify-content: space-around;
    align-items: center;
    padding: 8px 0;
  }
  .icon-strip svg { width: 14px; height: 14px; }
  .contact-list {
    list-style: none;
    padding: 8px 12px;
    display: flex;
    flex-direction: column;
    justify-content: space-around;
    color: var(--white);
    font-size: 13.5px;
  }
  .accent-circle {
    position: absolute;
    left: 380px; top: 170px;
    width: 150px; height: 150px;
    border-radius: 50%;
    background: var(--orange);
  }
</style>
</head>
<body>
  <section class="card card-back" aria-label="Business card back">
    <svg class="corner" viewBox="0 0 540 330" aria-hidden="true">
      <polygon points="0,40 150,20 130,70 0,96" fill="var(--orange)"/>
      <polygon points="540,230 540,300 380,330 360,330 395,268" fill="var(--orange)"/>
    </svg>
    <div class="wordmark">TriVex</div>
  </section>

  <section class="card card-front" aria-label="Business card front">
    <div class="wordmark">TriVex</div>
    <div class="person">
      <p class="person-name">DANIEL K. <span class="surname">MARSH</span></p>
      <p class="person-role">Managing Director</p>
    </div>
    <div class="contact-band">
      <div class="icon-strip">
        <svg viewBox="0 0 16 16" aria-label="Phone"><path d="M4 1l3 3-2 2c1 2 3 4 5 5l2-2 3 3-2 2C7 14 2 9 2 3z" fill="#fff"/></svg>
        <svg viewBox="0 0 16 16" aria-label="Email"><rect x="1" y="3" width="14" height="10" fill="#fff"/><path d="M1 3l7 6 7-6" fill="none" stroke="#f7a83b" stroke-width="1.5"/></svg>
        <svg viewBox="0 0 16 16" aria-label="Website"><circle cx="8" cy="8" r="6.5" fill="none" stroke="#fff" stroke-width="1.5"/><path d="M1.5 8h13M8 1.5c-3 3-3 10 0 13M8 1.5c3 3 3 10 0 13" fill="none" stroke="#fff" stroke-width="1.2"/></svg>
      </div>
      <ul class="contact-list">
        <li>0438 615 247</li>
        <li>info@trivexplumbing.example.au</li>
        <li>trivexplumbing.example.au</li>
      </ul>
    </div>
    <div class="accent-circle" aria-hidden="true"></div>
  </section>
</body>
</html>
```